Silver Falcons Team Poster

I'm looking to design a team poster for my sons soccer team. The poster needs to be 6 feet long by 3 feet high. The team name needs to be at least 16 inches / the words "PKYL Region 58" & "Division 4" need to be on the poster at least 3 inches tall.

The team name is "Silver Falcons"

The kids are all 4 and five years old. This banner is for their soccer team. The Team uniforms are all black with a little red on them.

I was thinking of having the team name large and in Ninja style writing then having 5 Ninjas in various soccer kick / ninja poses. Each Ninja would have ninja head bands with the kids name on it / and their number in red on the chest. A black and red soccer ball would be incorporated in the poster like the Red Japanese / Chinese sun

The kids names and jersey numbers are listed below.

Frederick - 4
Liam - 2
Ethan P. - 7
Ethan K. - 6
Brodie - 3

If you have a better idea feel free to be as creative as you like. We could just have one ninja and soccer balls with numbers using the throwing star type shape as the red and black ball design. You could also use as many colors as you like / incorporate flames / zap, pow type comic elements etc. all up to you. Just make it cool!

Target Market(s)

The poster is for the team of 4 year old, boy soccer players. It should get them fired up and excited and something that the look forward to hanging up prior to each game this season.

Requirements
Must have
• 1) the name of the team - Silver Falcon's
2) The names of the players and their numbers (see above)
3) use of their uniform color scheme primary is black alternate is red
Frederick - 4
Liam - 2
Ethan P. - 7
Ethan K. - 6
Brodie - 3
4) the term "Region 58" no smaller than 3 inches
5) the term "Division 4" no smaller than 3 inches
Nice to have
• 1) cool use of a Ninja font style in the name
2) the coaches name incorporated into the image. her name is Maren Holtby so it could be either Coach Maren or Coach Holtby
3) our PKYL Region Badge incorporated into the ninja outfit (see badge below)
4) the PKYL logo on the bottom or top corner of the banner to support the league - see PKYL logo below.

```html
<!DOCTYPE html>
<html lang="en">
<head>
<meta charset="utf-8">
<title>Silver Falcons Team Banner</title>
<link rel="stylesheet" href="https://fonts.googleapis.com/css2?family=Bubblegum+Sans&family=Oswald:wght@500;600;700&display=swap">
<style>
  :root {
    --bg-dark: #161616;
    --bg-mid: #3a3a3a;
    --ink-white: #ffffff;
    --ink-grey: #bdbdbd;
    --title-red: #e3121b;
    --title-ice-top: #f4fbff;
    --title-ice-bottom: #8fc3e6;
    --title-edge: #1e5f9e;
    --ninja-fill: #101010;
    --ninja-edge: #ffffff;
    --jersey-red: #e3121b;
    --ball-light: #f2f2f2;
    --ball-dark: #7a7a7a;
    --badge-red: #c8141c;
  }
  html, body {
    margin: 0;
    padding: 0;
    overflow: hidden;
    background: var(--bg-dark);
  }
  .banner {
    position: relative;
    width: 1200px;
    height: 604px;
    overflow: hidden;
    background: radial-gradient(ellipse at 50% 40%, var(--bg-mid) 0%, #242424 55%, var(--bg-dark) 100%);
    font-family: "Oswald", "Arial Narrow", sans-serif;
  }
  .league-mark {
    position: absolute;
    top: 34px;
    width: 74px;
    height: 74px;
    border-radius: 50%;
    background: var(--badge-red);
    border: 4px solid var(--ink-white);
    display: flex;
    align-items: center;
    justify-content: center;
    color: var(--ink-white);
    font-weight: 600;
    font-size: 22px;
    letter-spacing: 1px;
  }
  .league-mark.left { left: 34px; }
  .league-mark.right { right: 34px; }
  .ball {
    position: absolute;
    border-radius: 50%;
    background: radial-gradient(circle at 38% 32%, var(--ball-light) 0%, #d0d0d0 55%, var(--ball-dark) 100%);
  }
  .ball.big-left { left: 378px; top: 36px; width: 108px; height: 108px; }
  .ball.big-right { left: 744px; top: 36px; width: 108px; height: 108px; }
  .ball.small-left { left: 106px; top: 170px; width: 72px; height: 72px; }
  .ball.small-right { left: 1026px; top: 170px; width: 72px; height: 72px; }
  .player {
    position: absolute;
    background: var(--ninja-fill);
    border: 4px solid var(--ninja-edge);
    border-radius: 46px 46px 22px 22px;
    box-sizing: border-box;
  }
  .player-name {
    position: absolute;
    top: 24px;
    left: 0;
    right: 0;
    text-align: center;
    color: var(--ink-white);
    font-weight: 600;
    font-size: 17px;
    letter-spacing: 0.5px;
  }
  .player-number {
    position: absolute;
    top: 58px;
    left: 0;
    right: 0;
    text-align: center;
    color: var(--jersey-red);
    font-weight: 700;
    font-size: 44px;
    line-height: 1;
  }
  .player.liam { left: 182px; top: 60px; width: 136px; height: 196px; transform: rotate(-8deg); }
  .player.brodie { left: 530px; top: 6px; width: 142px; height: 200px; }
  .player.ethan-p { left: 868px; top: 50px; width: 140px; height: 200px; transform: rotate(8deg); }
  .player.frederick { left: 92px; top: 266px; width: 164px; height: 200px; transform: rotate(-10deg); }
  .player.ethan-k { left: 944px; top: 262px; width: 164px; height: 204px; transform: rotate(10deg); }
  .team-title {
    position: absolute;
    left: 220px;
    top: 128px;
    width: 760px;
    height: 290px;
  }
  .team-title text {
    font-family: "Bubblegum Sans", "Comic Sans MS", cursive;
    text-anchor: middle;
    paint-order: stroke fill;
    stroke-linejoin: round;
  }
  .coach {
    position: absolute;
    left: 0;
    right: 0;
    top: 440px;
    text-align: center;
    color: var(--ink-white);
    font-weight: 600;
    font-size: 36px;
    letter-spacing: 0.5px;
  }
  .region {
    position: absolute;
    left: 0;
    right: 0;
    top: 505px;
    text-align: center;
    color: var(--ink-grey);
    font-weight: 500;
    font-size: 34px;
    letter-spacing: 1px;
  }
  .division {
    position: absolute;
    left: 0;
    right: 0;
    top: 550px;
    text-align: center;
    color: var(--ink-grey);
    font-weight: 500;
    font-size: 24px;
    letter-spacing: 1px;
  }
</style>
</head>
<body>
<main class="banner">
  <div class="league-mark left">PKYL</div>
  <div class="league-mark right">PKYL</div>

  <div class="ball big-left" role="img" aria-label="Soccer ball"></div>
  <div class="ball big-right" role="img" aria-label="Soccer ball"></div>
  <div class="ball small-left" role="img" aria-label="Soccer ball"></div>
  <div class="ball small-right" role="img" aria-label="Soccer ball"></div>

  <div class="player liam" role="img" aria-label="Cartoon ninja player with headband"><span class="player-name">LIAM</span><span class="player-number">2</span></div>
  <div class="player brodie" role="img" aria-label="Cartoon ninja player with headband"><span class="player-name">BRODIE</span><span class="player-number">3</span></div>
  <div class="player ethan-p" role="img" aria-label="Cartoon ninja player with sunglasses"><span class="player-name">ETHAN P.</span><span class="player-number">7</span></div>
  <div class="player frederick" role="img" aria-label="Cartoon ninja player with headband"><span class="player-name">FREDERICK</span><span class="player-number">4</span></div>
  <div class="player ethan-k" role="img" aria-label="Cartoon ninja player with headband"><span class="player-name">ETHAN K.</span><span class="player-number">6</span></div>

  <svg class="team-title" viewBox="0 0 760 290" aria-label="Silver Falcons">
    <defs>
      <linearGradient id="ice" x1="0" y1="0" x2="0" y2="1">
        <stop offset="0" stop-color="#f4fbff"/>
        <stop offset="1" stop-color="#8fc3e6"/>
      </linearGradient>
    </defs>
    <g>
      <text x="380" y="112" font-size="128" textLength="560" lengthAdjust="spacingAndGlyphs" fill="none" stroke="#e3121b" stroke-width="30">SILVER</text>
      <text x="380" y="112" font-size="128" textLength="560" lengthAdjust="spacingAndGlyphs" fill="url(#ice)" stroke="#1e5f9e" stroke-width="4">SILVER</text>
      <text x="380" y="250" font-size="150" textLength="700" lengthAdjust="spacingAndGlyphs" fill="none" stroke="#e3121b" stroke-width="30">FALCONS</text>
      <text x="380" y="250" font-size="150" textLength="700" lengthAdjust="spacingAndGlyphs" fill="url(#ice)" stroke="#1e5f9e" stroke-width="4">FALCONS</text>
    </g>
  </svg>

  <div class="coach">COACH MAREN HOLTBY</div>
  <div class="region">PKYL REGION 58</div>
  <div class="division">DIVISION 4</div>
</main>
</body>
</html>
```